political campaign tax exemption on school taxes that dont have kids in the district

Velmora School Board Races

Taxes, Taxes, Taxes!
Everyone pays them!
You have tax exemption for the elderly.
You have tax exemption for the veterans.
What about tax exemptions for you?

In Texas, a governing entity, has the option of giving a 20 percent tax exemption. Our current school board, hasnt offered it you! We will!

Can we count on your vote? You can count on ours!
small discloure (political ad paid by candidates)

attached are the candidates for this exemption

Political

• need to include disclaimer at bottom.

political ad paid by candidate

```html
<!DOCTYPE html>
<html lang="en">
<head>
<meta charset="utf-8">
<title>Velmora School Board Races – Tax Exemption</title>
<link href="https://fonts.googleapis.com/css2?family=Anton&family=Oswald:wght@500;700&display=swap" rel="stylesheet">
<style>
  :root{
    --red:#d6244d;
    --green:#3ea53f;
    --blue:#1c4f90;
    --navy:#14295a;
    --white:#ffffff;
    --gold:#f2b01e;
    --frame:#e6e6e6;
  }
  *{margin:0;padding:0;box-sizing:border-box;}
  html,body{width:1200px;height:932px;overflow:hidden;background:var(--frame);}
  .flyer{position:absolute;left:12px;top:12px;width:1176px;height:908px;background:var(--blue);overflow:hidden;font-family:'Oswald',sans-serif;color:var(--white);}
  .headline{position:absolute;left:0;top:0;width:100%;height:252px;background:var(--red);}
  .taxes-small{position:absolute;font-family:'Anton',sans-serif;line-height:1;}
  .taxes-small.one{left:150px;top:28px;font-size:58px;}
  .taxes-small.two{left:60px;top:86px;font-size:96px;}
  .taxes-big{position:absolute;left:318px;top:0;font-family:'Anton',sans-serif;font-size:200px;line-height:1;letter-spacing:2px;}
  .pays{position:absolute;left:876px;top:56px;width:270px;text-align:center;font-family:'Oswald',sans-serif;font-weight:700;font-size:42px;line-height:1.15;}
  .exempt-band{position:absolute;left:0;top:252px;width:100%;height:52px;background:var(--green);display:flex;justify-content:space-between;align-items:center;padding:0 38px 0 26px;font-weight:500;font-size:29px;}
  .question{position:absolute;left:16px;top:336px;width:790px;height:190px;background:var(--red);}
  .question h2{position:absolute;left:14px;top:4px;font-family:'Anton',sans-serif;font-weight:400;line-height:1;}
  .question .line1{display:block;font-size:66px;}
  .question .line2{display:block;font-size:104px;}
  .promise{position:absolute;left:830px;top:346px;width:324px;text-align:center;font-weight:500;font-size:28px;line-height:1.12;}
  .candidates{position:absolute;left:100px;top:608px;width:1000px;height:200px;}
  .card{position:absolute;top:0;display:flex;flex-direction:column;justify-content:center;align-items:center;text-align:center;font-family:'Anton',sans-serif;}
  .card small{font-family:'Oswald',sans-serif;font-weight:500;font-size:15px;margin-top:6px;}
  .card.alvarez{left:0;top:40px;width:210px;height:108px;background:var(--white);color:var(--blue);font-size:40px;line-height:1;}
  .card.alvarez small{color:var(--red);}
  .card.ibarra{left:258px;top:36px;width:218px;height:116px;background:var(--red);color:var(--white);font-size:42px;line-height:1;}
  .card.elias{left:550px;top:14px;width:176px;height:170px;background:var(--navy);color:var(--white);font-size:50px;line-height:1;}
  .card.tomas{left:780px;top:6px;width:192px;height:180px;background:var(--navy);color:var(--gold);font-size:46px;line-height:1;border:3px solid var(--gold);}
  .card.tomas small{color:var(--white);}
  .rule{position:absolute;left:16px;top:840px;width:1144px;height:3px;background:var(--white);}
  .footer{position:absolute;left:16px;top:852px;width:1144px;display:flex;justify-content:space-between;align-items:center;}
  .footer .ask{font-weight:700;font-size:26px;letter-spacing:2px;text-decoration:underline;text-underline-offset:4px;}
  .footer .disclaimer{font-weight:700;font-size:20px;}
</style>
</head>
<body>
<main class="flyer">
  <header class="headline">
    <span class="taxes-small one">TAXES</span>
    <span class="taxes-small two">TAXES</span>
    <h1 class="taxes-big">TAXES</h1>
    <p class="pays">EVERYONE PAYS<br>THEM!</p>
  </header>
  <section class="exempt-band">
    <span>YOU HAVE TAX EXEMPTION FOR THE ELDERLY</span>
    <span>YOU HAVE TAX EXEMPTION FOR THE VETERANS</span>
  </section>
  <section class="question">
    <h2><span class="line1">WHAT ABOUT TAX EXEMPTIONS</span><span class="line2">FOR YOU?</span></h2>
  </section>
  <p class="promise">IN TEXAS, A GOVERNING ENTITY, HAS THE OPTION OF GIVING A 20 PERCENT TAX EXEMPTION. OUR CURRENT SCHOOL BOARD, HASN'T OFFERED IT YOU! WE WILL!</p>
  <section class="candidates" aria-label="Velmora School Board candidates">
    <div class="card alvarez">Mateo Alvarez<small>Place 1</small></div>
    <div class="card ibarra">RAFAEL IBARRA<small>Place 2</small></div>
    <div class="card elias">ELIAS<small>Place 3</small></div>
    <div class="card tomas">TOMAS<small>Place 4</small></div>
  </section>
  <div class="rule"></div>
  <footer class="footer">
    <span class="ask">CAN WE COUNT ON YOUR VOTE? YOU CAN COUNT ON OURS!</span>
    <span class="disclaimer">POLITICAL AD PAID BY CANDIDATES</span>
  </footer>
</main>
</body>
</html>
```